Personal Pagewell Banner

I am creating a personal brand for myself. I want a pagewell banner that inspires and motivates people to reach their epic awesomeness. I am creating and designing my personal brand. It can be a background with words on a scenery a picture or 3d graphic. If someone looked at it, they should say it is aggressively epic and motivating. It should be dramatic and bold.
My personal goal is to help as many people reach financial freedom as possible, and challenge and break their own limiting beliefs. This personal brand will be integrated into my chirplo, workNest, and professional pagewell fanpage (in addition to personal page). My goals are to open up a school for the underpriveleged children, develop my network marketing company team, and become a billionaire in the process. I want to attract people to me that really identify with doing what most think is impossible in terms of personal growth, impact to the world and financial wealth.
Updates

I have updated my brief with more background, and added a new comment to the discussion section to give you more to work with.

Reason: To give designers more time and to create a second and third place prize.

Reason: I am giving designers time to submit more designs

Target Market(s)

business professionals, and people with an entrepreneurial spirit.

Industry/Entity Type

Financial

Requirements
Must have
• It must be the exact dimensions required for pagewell banners. It should not be bigger or smaller. exact!!!

```html
<!DOCTYPE html>
<html lang="en">
<head>
<meta charset="utf-8">
<title>Your Brand – Pagewell</title>
<link href="https://fonts.googleapis.com/css2?family=Arimo:wght@400;700&family=Delius&display=swap" rel="stylesheet">
<style>
:root{
  --page-bg:#e9ebf2;
  --bar-top:#5470ad;
  --bar-bottom:#3b5998;
  --bar-line:#2f477a;
  --white:#ffffff;
  --ink:#1c2a47;
  --muted:#6b7385;
  --link:#3b5998;
  --panel:#ffffff;
  --panel-soft:#f1f3f8;
  --border:#c7ccd8;
  --tile:#7f7f7f;
  --tile-num:#9d9d9d;
  --sky-top:#4f87bf;
  --sky-mid:#a9cbe6;
  --haze:#e8e6df;
  --desert:#b98549;
  --rock:#a4582a;
  --year:#7a8bb8;
  --rail:#c9cfe1;
  --rail-on:#5b6fa8;
  --btn:#f3f4f6;
}
*{box-sizing:border-box;margin:0;padding:0}
html,body{width:1200px;height:559px;overflow:hidden}
body{background:var(--page-bg);font-family:"Arimo",Arial,sans-serif;position:relative;color:var(--ink)}

.top-bar{position:absolute;left:0;top:0;width:1200px;height:41px;background:linear-gradient(var(--bar-top),var(--bar-bottom));border-bottom:1px solid var(--bar-line)}
.brand-name{position:absolute;left:104px;top:12px;color:var(--white);font-size:14px;font-weight:700}
.search{position:absolute;left:175px;top:8px;width:549px;height:23px;background:var(--white);border:1px solid var(--bar-line);font-size:14px;padding:3px 7px;color:#111}
.search svg{position:absolute;right:6px;top:4px}
.bar-icons{position:absolute;left:848px;top:10px;display:flex;gap:9px}
.bar-links{position:absolute;left:944px;top:13px;display:flex;gap:16px;color:#d8dfee;font-size:12px;font-weight:700}
.bar-tools{position:absolute;left:1034px;top:12px;display:flex;gap:14px}

.page{position:absolute;left:144px;top:42px;width:805px;height:473px;background:var(--panel);border:1px solid var(--border);border-top:none}
.cover{position:absolute;left:0;top:0;width:805px;height:295px;overflow:hidden;
  background:linear-gradient(180deg,var(--sky-top) 0%,var(--sky-mid) 55%,var(--haze) 78%,var(--desert) 100%)}
.cover::after{content:"";position:absolute;right:0;top:120px;width:190px;height:175px;background:linear-gradient(160deg,var(--rock),#7b3d1c);border-radius:40% 0 0 0;opacity:.85}
.tagline{position:absolute;left:78px;top:36px;color:#eef2f6;font-family:"Delius",cursive;font-size:38px;white-space:nowrap;z-index:1}
.tagline b{font-size:60px;font-weight:400}

.avatar{position:absolute;left:22px;top:196px;width:170px;height:169px;background:var(--white);border:1px solid #9aa0ad;border-radius:3px;z-index:2}
.page-title{position:absolute;left:205px;top:330px;font-size:20px;font-weight:700}
.page-stats{position:absolute;left:205px;top:356px;font-size:11px;color:var(--muted)}
.btn{position:absolute;top:312px;height:24px;background:var(--btn);border:1px solid #999;border-radius:2px;font-size:13px;font-weight:700;color:#333;display:flex;align-items:center}
.btn-liked{left:595px;width:66px;padding-left:7px;gap:4px}
.btn-message{left:670px;width:112px;padding-left:8px}
.btn-message .opts{position:absolute;right:0;top:0;height:22px;width:40px;border-left:1px solid #bbb;display:flex;align-items:center;justify-content:center;gap:4px}

.about{position:absolute;left:0;top:368px;width:311px;height:70px;background:var(--panel-soft);border-top:1px solid #dde0e8;border-bottom:1px solid #dde0e8;padding:6px 25px;font-size:11px;line-height:16px}
.about .kind{color:var(--muted)}
.about a,.about-links a{color:var(--link);text-decoration:none}
.about-links{position:absolute;left:43px;top:448px;font-size:11px}

.tiles{position:absolute;left:318px;top:368px;display:flex;gap:7px}
.tile{width:105px;position:relative}
.tile .face{height:70px;background:var(--tile);border:1px solid #666;color:var(--tile-num);font-size:44px;display:flex;align-items:center;justify-content:center}
.tile .face.likes{background:var(--panel-soft);border-color:#d5d9e3;color:var(--ink);font-size:22px;font-weight:700;gap:6px}
.tile .label{font-size:11px;color:var(--link);margin-top:9px}
.tile-more{width:36px;height:70px;background:var(--panel-soft);border:1px solid #d5d9e3;position:relative}
.tile-more span{position:absolute;left:-5px;top:26px;width:28px;height:17px;background:var(--white);border:1px solid #8a93a8;font-size:11px;padding:1px 4px;color:#333}

.spine{position:absolute;left:545px;top:515px;width:3px;height:44px;background:var(--rail)}
.highlights{position:absolute;left:506px;top:530px;width:81px;height:21px;background:var(--page-bg);border:1px solid var(--rail);border-radius:2px;font-size:11px;color:var(--year);padding:4px 0 0 8px}

.years{position:absolute;left:960px;top:45px;border-left:4px solid var(--rail);list-style:none;font-size:11px;color:var(--year)}
.years li{height:21.8px;padding:4px 0 0 7px}
.years li.current{color:var(--rail-on);font-weight:700;border-left:4px solid var(--rail-on);margin-left:-4px}
</style>
</head>
<body>
<header class="top-bar">
  <span class="brand-name">Pagewell</span>
  <div class="search">Your Brand
    <svg width="12" height="12" viewBox="0 0 12 12"><circle cx="5" cy="5" r="3.8" fill="none" stroke="#777" stroke-width="1.4"/><line x1="8" y1="8" x2="11" y2="11" stroke="#777" stroke-width="1.6"/></svg>
  </div>
  <div class="bar-icons">
    <svg width="22" height="18" viewBox="0 0 22 18"><circle cx="8" cy="6" r="4" fill="#22386a"/><path d="M1 17c0-5 14-5 14 0z" fill="#22386a"/><circle cx="15" cy="6" r="3.5" fill="#22386a"/></svg>
    <svg width="22" height="18" viewBox="0 0 22 18"><rect x="2" y="2" width="16" height="11" rx="2" fill="#22386a"/><path d="M5 13l0 4 5-4z" fill="#22386a"/></svg>
    <svg width="20" height="20" viewBox="0 0 20 20"><circle cx="10" cy="10" r="8.5" fill="#22386a"/><circle cx="10" cy="10" r="8.5" fill="none" stroke="#4d66a0"/></svg>
  </div>
  <nav class="bar-links"><span>Home</span><span>Rowan</span></nav>
  <div class="bar-tools">
    <svg width="16" height="13" viewBox="0 0 16 13"><rect x="1" y="1" width="7" height="11" fill="#d8dfee"/><rect x="9" y="3" width="6" height="2" fill="#d8dfee"/><rect x="9" y="7" width="6" height="2" fill="#d8dfee"/></svg>
    <svg width="13" height="13" viewBox="0 0 13 13"><circle cx="6.5" cy="6.5" r="4" fill="none" stroke="#d8dfee" stroke-width="3" stroke-dasharray="2 1.2"/><circle cx="6.5" cy="6.5" r="2" fill="#d8dfee"/></svg>
  </div>
</header>

<main class="page">
  <div class="cover" role="img" aria-label="Cover photo: a businessman with a briefcase standing on the edge of a red rock cliff above a wide desert under a blue sky">
    <p class="tagline">Release your <b>EPIC</b></p>
  </div>
  <div class="avatar" role="img" aria-label="Profile picture placeholder"></div>

  <h1 class="page-title">Your Brand</h1>
  <p class="page-stats">21,942,038 likes · 344,909 talking about this · 4,499,542 were here</p>

  <div class="btn btn-liked"><svg width="10" height="9" viewBox="0 0 10 9"><path d="M1 5l3 3 5-7" fill="none" stroke="#444" stroke-width="1.8"/></svg>Liked</div>
  <div class="btn btn-message">Message
    <span class="opts"><svg width="10" height="10" viewBox="0 0 10 10"><circle cx="5" cy="5" r="3" fill="none" stroke="#333" stroke-width="2.4" stroke-dasharray="1.6 0.9"/></svg><svg width="8" height="5" viewBox="0 0 8 5"><path d="M0 0h8L4 5z" fill="#555"/></svg></span>
  </div>

  <section class="about">
    <div class="kind">Product/Service</div>
    <div>Our product is awesome... Try it</div>
    <a href="#">http://brightgoods.com/</a>
  </section>
  <div class="about-links"><a href="#">About</a> · <a href="#">Suggest an Edit</a></div>

  <div class="tiles">
    <div class="tile"><div class="face">1</div><div class="label">Photos</div></div>
    <div class="tile"><div class="face">2</div><div class="label">Videos</div></div>
    <div class="tile"><div class="face likes"><svg width="14" height="14" viewBox="0 0 14 14"><rect x="1" y="1" width="12" height="12" fill="#6d84b4"/></svg>21m</div><div class="label">Likes</div></div>
    <div class="tile"><div class="face">4</div><div class="label">Events</div></div>
    <div class="tile-more"><span>3 ▾</span></div>
  </div>
</main>

<div class="spine"></div>
<div class="highlights">Highlights ▾</div>

<ul class="years">
  <li class="current">Recent</li><li>2013</li><li>2012</li><li>2011</li><li>2010</li><li>2009</li><li>2008</li><li>2006</li><li>2004</li><li>2003</li><li>2001</li><li>2000</li><li>1998</li><li>1997</li><li>1996</li><li>1995</li><li>1992</li><li>1997</li><li>1988</li><li>1987</li><li>1984</li><li>1983</li><li>1982</li><li>Opened</li>
</ul>
</body>
</html>
```